San Francisco Pet Care Non Profit

Business Card Design for non profit organization.
We are a mobile pet care team who supports and attends to pets whose owners are homeless. Thanks for your help and creativity.

Industry/Entity Type

Non Profit

Contact Information for Business Card

Marisol Keddy
President
2871 Larkmoor Street, #512
San Francisco, CA 94187
phone: 415-729-3846
fax: 415-781-4052
marisol@tidywagonvan.org
website: tidywagonvan.org
facebook: facebook.com/TidyWagonVan

Font styles to use
Serif
Sans Serif

Colors

Designer to choose colors to be used in the design.

Requirements
Must have
• above details and attached logo

```html
<!DOCTYPE html>
<html lang="en">
<head>
<meta charset="utf-8">
<title>TidyWagonVan Business Card</title>
<link href="https://fonts.googleapis.com/css2?family=Open+Sans:wght@400;700;800&display=swap" rel="stylesheet">
<style>
  :root {
    --stage: #b4b4b4;
    --ink: #231f20;
    --sky: #00aeef;
    --paper: #ffffff;
  }
  * { box-sizing: border-box; margin: 0; padding: 0; }
  html, body { width: 1200px; height: 923px; overflow: hidden; }
  body {
    background: var(--stage);
    font-family: "Open Sans", Arial, sans-serif;
    position: relative;
  }
  .card {
    position: absolute;
    width: 700px;
    height: 400px;
    border-radius: 34px;
    overflow: hidden;
  }
  .card-back { left: 440px; top: 40px; background: var(--ink); }
  .card-front { left: 60px; top: 480px; background: var(--paper); }

  .back-brand {
    position: absolute; left: 0; right: 0; top: 130px;
    display: flex; align-items: center; justify-content: center; gap: 16px;
    color: var(--paper); font-weight: 800; font-size: 48px;
  }
  .brand-dot { width: 34px; height: 34px; border-radius: 50%; background: var(--sky); }
  .back-url {
    position: absolute; left: 0; right: 0; top: 300px; text-align: center;
    color: var(--paper); font-size: 20px; letter-spacing: 5px;
  }

  .front-wave { position: absolute; inset: 0; }
  .front-brand {
    position: absolute; left: 70px; top: 38px;
    display: flex; align-items: center; gap: 16px;
    color: var(--sky); font-weight: 800; font-size: 50px; line-height: 1;
  }
  .front-brand .brand-dot { width: 44px; height: 44px; }
  .tagline {
    position: absolute; left: 0; width: 600px; top: 104px; text-align: right;
    color: var(--ink); font-weight: 800; font-size: 22px;
  }
  .person {
    position: absolute; left: 0; right: 0; top: 162px; text-align: center;
    font-weight: 800; font-size: 26px;
  }
  .person-name { color: var(--sky); }
  .person-title { color: var(--ink); }
  .contacts {
    position: absolute; left: 0; right: 0; top: 282px;
    color: var(--paper); font-size: 17px; text-align: center; line-height: 32px;
  }
  .contact-row { display: flex; justify-content: center; gap: 20px; white-space: nowrap; }
  .contact-item { display: inline-flex; align-items: center; gap: 6px; }
  .contact-item svg { width: 16px; height: 16px; }
</style>
</head>
<body>

<section class="card card-back">
  <div class="back-brand"><span class="brand-dot"></span>TidyWagonVan</div>
  <div class="back-url">www.tidywagonvan.org</div>
</section>

<section class="card card-front">
  <svg class="front-wave" viewBox="0 0 700 400" preserveAspectRatio="none">
    <path d="M0,148 Q300,300 700,262 L700,400 L0,400 Z" fill="var(--sky)"/>
    <path d="M0,112 Q290,292 700,256 Q290,282 0,138 Z" fill="var(--ink)"/>
  </svg>

  <div class="front-brand"><span class="brand-dot"></span>TidyWagonVan</div>
  <div class="tagline">Mobile Pet Care Team</div>
  <div class="person"><span class="person-name">Marisol Keddy,</span> <span class="person-title">President</span></div>

  <div class="contacts">
    <div class="contact-row">
      <span class="contact-item">
        <svg viewBox="0 0 16 16"><path d="M4 1.5 6.5 5 5 6.5c.8 1.8 2.3 3.3 4.5 4.5L11 9.5l3.5 2.5-1.5 2.5C8 14.5 1.5 8 1.5 3Z" fill="none" stroke="currentColor" stroke-width="1.5"/></svg>
        415-729-3846
      </span>
      <span class="contact-item">
        <svg viewBox="0 0 16 16"><rect x="4" y="1" width="8" height="5" fill="currentColor"/><rect x="1" y="6" width="14" height="6" rx="1" fill="currentColor"/><rect x="4" y="10" width="8" height="5" fill="currentColor" stroke="#00aeef"/></svg>
        415-781-4052
      </span>
    </div>
    <div class="contact-row">
      <span class="contact-item">
        <svg viewBox="0 0 16 16"><rect x="1" y="3" width="14" height="10" fill="none" stroke="currentColor" stroke-width="1.5"/><path d="M1 3l7 6 7-6" fill="none" stroke="currentColor" stroke-width="1.5"/></svg>
        marisol@tidywagonvan.org
      </span>
      <span class="contact-item">
        <svg viewBox="0 0 16 16"><circle cx="8" cy="8" r="6.5" fill="none" stroke="currentColor" stroke-width="1.3"/><ellipse cx="8" cy="8" rx="3" ry="6.5" fill="none" stroke="currentColor" stroke-width="1.2"/><path d="M1.5 8h13" stroke="currentColor" stroke-width="1.2"/></svg>
        www.tidywagonvan.org
      </span>
      <span class="contact-item">
        <svg viewBox="0 0 16 16"><circle cx="8" cy="8" r="7" fill="none" stroke="currentColor" stroke-width="1.5"/></svg>
        /TidyWagonVan
      </span>
    </div>
    <div class="contact-row">2871 Larkmoor Street, #512, San Francisco, CA 94187</div>
  </div>
</section>

</body>
</html>
```